Real Estate Agent need For Sale sign for

We need a for sale sign for our team based in Los Angeles, CA. My team name is Corvalen Real Estate Group. Also known as Team Corvalen. We are also under the Brandt Osgood umbrella. We are a real estate team that enjoys contributing to the world through supporting homeowners and sellers achieve their real estate goals. The final design should communicate trust, integrity, and loyalty.
Need to have our team name on there: Team Corvalen, phone number 323-555-0172, my licensed number DRE #8062714 on there. The size of the sign will be 32X36.
Target Market(s)
Home buyers and sellers.
Industry/Entity Type
Real Estate Agent
Colors
Designer to choose colors to be used in the design.
Look and feel

```html
<!DOCTYPE html>
<html lang="en">
<head>
<meta charset="utf-8">
<title>Corvalen Real Estate Group – For Sale Sign</title>
<link rel="stylesheet" href="https://fonts.googleapis.com/css2?family=Righteous&family=Anton&family=Roboto:wght@700&display=swap">
<style>
  :root {
    --backdrop: #a9a9a9;
    --sign-blue: #02509b;
    --sign-red: #ec1c24;
    --sign-white: #ffffff;
  }
  * { margin: 0; padding: 0; box-sizing: border-box; }
  html, body {
    width: 1200px;
    height: 900px;
    overflow: hidden;
    background: var(--backdrop);
  }
  .sign {
    position: absolute;
    left: 176px;
    top: 73px;
    width: 850px;
    height: 755px;
    background: var(--sign-red);
    box-shadow: 0 18px 24px -12px rgba(0, 0, 0, 0.45);
    color: var(--sign-white);
  }
  .sign__panels {
    position: absolute;
    inset: 0;
    width: 850px;
    height: 755px;
  }
  .sign__panel--blue { fill: var(--sign-blue); }
  .sign__panel--stripe { fill: var(--sign-white); }

  .team-name {
    position: absolute;
    left: 0;
    width: 850px;
    text-align: center;
    font-family: "Righteous", sans-serif;
    font-weight: 400;
    color: var(--sign-white);
  }
  .team-name__primary {
    top: 200px;
    font-size: 150px;
    line-height: 1;
    letter-spacing: 2px;
  }
  .team-name__secondary {
    top: 340px;
    font-size: 54px;
    line-height: 1;
    letter-spacing: 4px;
  }

  .brokerage {
    position: absolute;
    left: 55px;
    top: 570px;
    font-family: "Righteous", sans-serif;
    font-weight: 400;
    font-size: 32px;
    line-height: 1;
    color: var(--sign-white);
  }
  .license {
    position: absolute;
    right: 56px;
    top: 576px;
    font-family: "Roboto", sans-serif;
    font-weight: 700;
    font-size: 28px;
    letter-spacing: 1px;
    line-height: 1;
  }
  .phone {
    position: absolute;
    left: 0;
    width: 850px;
    top: 628px;
    text-align: center;
    font-family: "Anton", sans-serif;
    font-size: 88px;
    line-height: 1;
    letter-spacing: 1px;
  }
</style>
</head>
<body>
  <div class="sign">
    <svg class="sign__panels" viewBox="0 0 850 755" aria-hidden="true">
      <polygon class="sign__panel--stripe" points="0,396 414,552 850,396 850,392 414,540 0,392"/>
      <polygon class="sign__panel--blue" points="0,0 850,0 850,393 414,535 0,393"/>
    </svg>

    <div class="team-name team-name__primary">Corvalen</div>
    <div class="team-name team-name__secondary">REAL ESTATE GROUP</div>

    <div class="brokerage">Brandt Osgood</div>
    <div class="license">DRE #8062714</div>
    <div class="phone">Call Us: 323-555-0172</div>
  </div>
</body>
</html>
```